144" w/base kestavan wrap for Electrical contractor

Professional vehicle wrap design. vehicle is white. ive added my logo and a sticker i use. do NOT include "HIGH VOLTAGE" it is only on there for the sticker design. the bullet points do not need to match but thats at least a good start. if you want to add more please let me know and i can come up with plenty more. i think i would like to do a matte background

Target Market(s)

High end residnetial

Industry/Entity Type

electrical contractor

Font styles to use
Sans Serif

Colors
0054AA
0677BA
7BADD7
CADEEF
E8F1F8
FFC000
F8CF3A
FAE287
FDF2CF
FEFAEE

Requirements
Must have
• My logo and phone number large and easy to read - the phrase "Premier Electrical Contractor Serving SWFL For All Your Electrical Needs
Nice to have
• some back ground design. do not want 100% wrapped 75% at most for vehical coverage
Should not have
• 100% coverage

```html
<!DOCTYPE html>
<html lang="en">
<head>
<meta charset="utf-8">
<title>Norvel Electric – Kestavan Wrap</title>
<link rel="stylesheet" href="https://fonts.googleapis.com/css2?family=Montserrat:wght@600;700;800&family=Oswald:wght@500&family=Orbitron:wght@700&display=swap">
<style>
  :root{
    --wrap-blue:#1f3a8f;
    --wrap-gold:#e6c07f;
    --wrap-gold-light:#f4e2bf;
    --van-white:#f7f7f7;
    --van-line:#c9c9c9;
    --glass:#9a9a9a;
    --trim:#151515;
    --hub:#8d8d8d;
    --tail-red:#b3141b;
    --bg:#ffffff;
  }
  html,body{margin:0;padding:0;width:1200px;height:1200px;overflow:hidden;background:var(--bg);}
  .canvas{display:block;width:1200px;height:1200px;}
  .tagline{font-family:"Montserrat",sans-serif;font-weight:600;fill:var(--wrap-blue);}
  .phone{font-family:"Orbitron","Montserrat",sans-serif;font-weight:700;}
  .brand-name{font-family:"Montserrat",sans-serif;font-weight:800;fill:var(--wrap-blue);}
  .license{font-family:"Montserrat",sans-serif;font-weight:600;fill:var(--wrap-blue);}
  .license-no{font-family:"Montserrat",sans-serif;font-weight:700;fill:var(--wrap-blue);}
  .services{font-family:"Montserrat",sans-serif;font-weight:600;fill:#fff;}
  .slogan{font-family:"Oswald",sans-serif;font-weight:500;letter-spacing:1px;}
</style>
</head>
<body>
<svg class="canvas" viewBox="0 0 1200 1200" xmlns="http://www.w3.org/2000/svg">

  <!-- SIDE ELEVATION -->
  <g class="side-view">
    <ellipse class="ground-shadow" cx="600" cy="551" rx="500" ry="4" fill="#222"/>
    <path class="van-body" d="M106,478 L108,382 Q112,350 150,335 Q230,300 300,262 L360,185 Q420,115 490,98 L1022,92 Q1045,95 1052,118 L1078,300 L1082,440 L1090,468 L106,478 Z" fill="var(--van-white)" stroke="var(--van-line)" stroke-width="1.5"/>
    <!-- rear gold sweep with a thin blue edge stripe -->
    <polygon class="wrap-edge-stripe" points="700,368 1058,176 1060,192 730,368" fill="var(--wrap-blue)"/>
    <polygon class="wrap-gold-field" points="760,368 1060,204 1062,366" fill="var(--wrap-gold)"/>
    <!-- blue band -->
    <polygon class="wrap-band" points="108,395 1055,366 1058,392 108,412" fill="var(--wrap-blue)"/>
    <!-- lower trim -->
    <polygon class="rocker" points="104,412 1080,392 1085,440 1100,465 104,478" fill="var(--trim)"/>
    <polygon class="wrap-rocker-gold" points="315,445 1040,430 1050,465 335,485" fill="var(--wrap-gold)"/>
    <!-- windows -->
    <polygon class="window" points="370,182 460,176 465,285 300,308" fill="var(--glass)" stroke="#222" stroke-width="3"/>
    <polygon class="windshield" points="355,190 292,300 250,320 305,250" fill="#3a3a3a"/>
    <rect class="tail-light" x="1055" y="298" width="26" height="98" rx="3" fill="var(--tail-red)"/>
    <!-- panel seams -->
    <path class="seams" d="M488,98 L488,480 M760,94 L760,470 M288,310 L288,470" stroke="var(--van-line)" stroke-width="1.2" fill="none"/>

    <text class="tagline" x="523" y="158" font-size="12">FOR ALL YOUR ELECTRICAL NEEDS -</text>
    <text class="phone" x="757" y="160" font-size="24" fill="var(--wrap-blue)" textLength="225">555 014 0188</text>

    <text class="brand-name" x="528" y="270" font-size="58" textLength="206" lengthAdjust="spacingAndGlyphs">NORVEL</text>
    <text class="brand-name" x="528" y="332" font-size="40" textLength="206" lengthAdjust="spacingAndGlyphs">ELECTRIC</text>

    <text class="license" x="313" y="348" font-size="12">license and insured</text>
    <text class="license-no" x="313" y="369" font-size="21">EC10457721</text>

    <text class="services" x="310" y="400" font-size="11.5" transform="rotate(-1.2 310 400)" textLength="517">Generators - Solar - EV Chargers - Accent lighting - Renovation - Services / Repair</text>
    <text class="slogan" x="365" y="472" font-size="19" fill="var(--wrap-gold-light)" transform="rotate(-0.8 365 472)" textLength="415">PREMIER ELECTRICAL CONTRACTOR SERVING SWFL</text>

    <g class="wheel">
      <circle cx="245" cy="486" r="64" fill="var(--trim)"/>
      <circle cx="245" cy="486" r="38" fill="var(--hub)"/>
    </g>
    <g class="wheel">
      <circle cx="885" cy="484" r="64" fill="var(--trim)"/>
      <circle cx="885" cy="484" r="38" fill="var(--hub)"/>
    </g>
  </g>

  <!-- REAR ELEVATION -->
  <g class="rear-view">
    <ellipse class="ground-shadow" cx="597" cy="1134" rx="215" ry="3" fill="#222"/>
    <rect class="tire" x="420" y="1080" width="48" height="48" rx="10" fill="var(--trim)"/>
    <rect class="tire" x="724" y="1080" width="48" height="48" rx="10" fill="var(--trim)"/>
    <path class="van-rear" d="M410,1000 L425,760 Q440,650 470,648 L735,648 Q762,650 772,760 L786,1000 Z" fill="var(--van-white)" stroke="var(--van-line)" stroke-width="1.5"/>
    <path class="wrap-gold-field" d="M424,760 Q440,835 470,838 L725,838 Q760,835 773,760 L780,935 L416,935 Z" fill="var(--wrap-gold)"/>
    <path class="wrap-band" d="M416,933 L780,933 L784,1060 Q782,1080 760,1082 L436,1082 Q414,1080 412,1060 Z" fill="var(--wrap-blue)"/>
    <rect class="bumper" x="406" y="1078" width="384" height="30" rx="6" fill="var(--trim)"/>
    <rect class="tail-light" x="408" y="880" width="18" height="112" rx="3" fill="var(--tail-red)"/>
    <rect class="tail-light" x="768" y="880" width="18" height="112" rx="3" fill="var(--tail-red)"/>
    <line class="door-seam" x1="597" y1="650" x2="597" y2="1080" stroke="var(--van-line)" stroke-width="1"/>
    <rect class="brake-light" x="562" y="642" width="70" height="6" rx="2" fill="var(--tail-red)"/>

    <text class="brand-name" x="597" y="762" font-size="52" text-anchor="middle" textLength="200" lengthAdjust="spacingAndGlyphs">NORVEL</text>
    <text class="brand-name" x="597" y="818" font-size="38" text-anchor="middle" textLength="200" lengthAdjust="spacingAndGlyphs">ELECTRIC</text>

    <text class="slogan" x="597" y="892" font-size="13" fill="#fff" text-anchor="middle" textLength="248">PREMIER ELECTRICAL CONTRACTOR SERVING SWFL</text>
    <text class="slogan" x="597" y="916" font-size="17" fill="#fff" text-anchor="middle" textLength="196">FOR ALL YOUR ELECTRICAL NEEDS</text>
    <text class="phone" x="597" y="984" font-size="34" fill="#fff" text-anchor="middle" textLength="285">555-014-0188</text>
    <text class="slogan" x="597" y="1031" font-size="10" fill="#fff" text-anchor="middle" textLength="300">SERVICE / REPAIR - RENOVATION - ACCENT LIGHTING - GENERATORS - SOLAR - EV CHARGERS</text>
  </g>
</svg>
</body>
</html>
```